Gourmet food company looking for a dazzling label for their premuim vinagrette dressings

Need a food label that will dazzle our customer and prove what a premium product we have. We make high end gourmet dressing for vegetables, fruit, meat, poultry and fish.

Our label will fit on a 250 mil Tolvenka Square bottle. Labels should be a 4x5 or even 5x5 depending on the design. Nutritionals, bar codes and company blurb will be supplied later. We really want to test you all's talent on this one and are very excited to see your renderings!

Our dressings are Champagne Pear Vinaigrette, White Balsmic Vinaigrette, Mojito Lime Vinaigrette, Creamy-Avacado Lime Vinaigrette, and Asian Sesame Vinaigrette. I hope these names will help you envision our product and kinda what we are looking for.
Updates

Thank you all so far for your renderings.I really don't want pictures if that helps. Our logo can be smaller and/or the name of the product bigger. Perhaps we can even redesign Velora and remove the leaf as I don't really care for what I see yet.So good luck and thanks Added Friday, August 19, 2016

I am still looking for that clean - elegant design for our product as our product is just that. If you look on the internet at vinegars and oils you will see many designs that are simple yet elegant. Creative lettering, bordering, color (can be black and white) and size will help accomplish this. So I invite you to use all your creativity and help me find just what we need.Many thanks Added Tuesday, August 23, 2016

Project Deadline Extended Reason: So many great designs coming in that I wanted a few extra days to tweek!Great job all Added Friday, August 26, 2016

Project Deadline Extended Reason: Very good designs thus far. We just need a few more days.Thanks Added Wednesday, August 31, 2016

Target Market(s)

High end grocery and specialty stores.

Our side panel on the label will say "At Velora we're fanatics for great flavors and are passionate about finding the best ingredients. From simple to elegant our products are "simply velora".

Industry/Entity Type

It Company

Font styles to use
Serif
Decorative
Script

Requirements
Must have
• A label that will draw the consumer to pick it up! Need something bold and elegant...
Nice to have
• Again, I really would like to have a label that pops. Since the bottle front is only about 2inches in width it will need some creativity. Would like something very simple and elegant.
• If the designer does not like the logo, please feel free to design without it!
Should not have
• Dark dark colors. We are selling dressing and we don't want any colors that may distort the contents.
• No stock photos for the front. I don't want our dressing to look like the others on the self. Brambleth Kitchen just uses lettering and a their packaging is eye catching

```html
<!DOCTYPE html>
<html lang="en">
<head>
<meta charset="utf-8">
<title>Velora Vinaigrette Labels – Proposals #3</title>
<link href="https://fonts.googleapis.com/css2?family=Montserrat:wght@400;500;600;700&family=Open+Sans:wght@500&family=Sacramento&display=swap" rel="stylesheet">
<style>
  :root {
    --page: #ffffff;
    --heading: #555555;
    --label-dark: #383534;
    --white: #ffffff;
    --muted-line: #8a8784;
    --avocado: #8aab8c;
    --sesame: #c9474a;
    --mojito: #bed957;
  }
  * { margin: 0; padding: 0; box-sizing: border-box; }
  html, body {
    width: 1200px; height: 1065px; overflow: hidden;
    background: var(--page);
  }
  .board { position: relative; width: 1200px; height: 1065px; }
  .board-title {
    position: absolute; top: 38px; left: 0; width: 100%;
    text-align: center;
    font: 500 21px/1 "Open Sans", sans-serif;
    color: var(--heading); letter-spacing: 0.5px;
  }
  .flavour { position: absolute; top: 0; width: 195px; height: 1065px; }
  .flavour--avocado { left: 159px; --accent: var(--avocado); }
  .flavour--sesame  { left: 501px; --accent: var(--sesame); }
  .flavour--mojito  { left: 838px; --accent: var(--mojito); }

  .neck-band {
    position: absolute; top: 255px; left: 38px; width: 118px; height: 33px;
    background: var(--accent);
    display: flex; align-items: center; justify-content: center;
    font: 600 10px/1 "Montserrat", sans-serif;
    letter-spacing: 2.5px; color: var(--white);
  }
  .front-label {
    position: absolute; top: 428px; left: 0; width: 195px; height: 485px;
    background: var(--label-dark);
  }
  .ribbon {
    position: absolute; top: 0; left: 22px; width: 150px; height: 307px;
    background: var(--accent);
    clip-path: polygon(0 0, 100% 0, 100% 100%, 50% 88%, 0 100%);
  }
  .brand {
    position: absolute; top: 10px; left: 0; width: 100%;
    text-align: center; color: var(--white);
    font: 600 15px/1 "Montserrat", sans-serif; letter-spacing: 4px;
  }
  .flavour-name {
    position: absolute; top: 62px; left: -10px; width: 215px;
    text-align: center; color: var(--white);
    font: 400 62px/0.9 "Sacramento", cursive;
  }
  .flavour-caption {
    position: absolute; top: 250px; left: 0; width: 100%;
    text-align: center; color: var(--white);
    font: 500 9.5px/1 "Montserrat", sans-serif; letter-spacing: 0.3px;
  }
  .product-type {
    position: absolute; top: 400px; left: 0; width: 100%;
    text-align: center; color: var(--white);
    font: 500 13px/1.15 "Montserrat", sans-serif; letter-spacing: 0.8px;
  }
  .product-type strong { font-weight: 700; display: block; }
  .rule { position: absolute; left: 22px; width: 150px; height: 1.5px; }
  .rule--top { top: 437px; background: var(--accent); }
  .rule--bottom { top: 467px; background: var(--muted-line); }
  .flavour--sesame .rule--bottom, .flavour--mojito .rule--bottom { background: var(--accent); }
  .net-weight {
    position: absolute; top: 446px; left: 0; width: 100%;
    text-align: center; color: var(--white);
    font: 500 13.5px/1 "Montserrat", sans-serif; letter-spacing: 0.6px;
  }
</style>
</head>
<body>
<main class="board">
  <h1 class="board-title">NEW PROPOSALS #3</h1>

  <section class="flavour flavour--avocado">
    <div class="neck-band">VELORA</div>
    <div class="front-label">
      <div class="ribbon"></div>
      <div class="brand">VELORA</div>
      <div class="flavour-name">lime<br>avocado</div>
      <div class="flavour-caption">LIME AVOCADO</div>
      <div class="product-type">HIGH QUALITY<strong>VINAIGRETTE</strong></div>
      <div class="rule rule--top"></div>
      <div class="net-weight">Net WT 250ml</div>
      <div class="rule rule--bottom"></div>
    </div>
  </section>

  <section class="flavour flavour--sesame">
    <div class="neck-band">VELORA</div>
    <div class="front-label">
      <div class="ribbon"></div>
      <div class="brand">VELORA</div>
      <div class="flavour-name">asian<br>sesame</div>
      <div class="flavour-caption">ASIAN SESAME</div>
      <div class="product-type">HIGH QUALITY<strong>VINAIGRETTE</strong></div>
      <div class="rule rule--top"></div>
      <div class="net-weight">Net WT 250ml</div>
      <div class="rule rule--bottom"></div>
    </div>
  </section>

  <section class="flavour flavour--mojito">
    <div class="neck-band">VELORA</div>
    <div class="front-label">
      <div class="ribbon"></div>
      <div class="brand">VELORA</div>
      <div class="flavour-name">lime<br>mojito</div>
      <div class="flavour-caption">LIME MOJITO</div>
      <div class="product-type">HIGH QUALITY<strong>VINAIGRETTE</strong></div>
      <div class="rule rule--top"></div>
      <div class="net-weight">Net WT 250ml</div>
      <div class="rule rule--bottom"></div>
    </div>
  </section>
</main>
</body>
</html>
```